Neue Verpackung für unsere Arbeitssocken :) | New packaging for our work socks :)
Zielgruppe
Wir sind eine Modefirma und suchen ein hochwertiges Design für unsere Arbeitssocken, unsere Zielgruppe sind Männer und Frauen.
We are a fashion company and looking for a high quality design for our work socks, our target group are men and women.
Aufgabenstellung
Die Datei 'cintas brunsdorff' zeigt unser jetziges Design. Das neue Design soll in Richtung der DUX Arbeitssocken gehen!
Logo, Texte und Farben können abgewandelt werden.
The file 'cintas brunsdorff' shows our current design. The new design should go in the direction of the DUX work socks!
Logo, texts and colors can be modified.

```html
<!DOCTYPE html>
<html lang="de">
<head>
<meta charset="utf-8">
<title>Brunsdorff Arbeitssocken – Banderole</title>
<link href="https://fonts.googleapis.com/css2?family=Montserrat:wght@500;700;800;900&display=swap" rel="stylesheet">
<style>
  :root {
    --yellow: #fec600;
    --black: #000000;
    --white: #ffffff;
    --backdrop: #e4e4e4;
  }
  * { margin: 0; padding: 0; box-sizing: border-box; }
  html, body { width: 1200px; height: 1080px; overflow: hidden; }
  body {
    background: var(--backdrop);
    font-family: "Montserrat", Arial, sans-serif;
    position: relative;
  }
  .sleeve {
    position: absolute;
    left: 47px; top: 376px;
    width: 1115px; height: 293px;
    background: var(--yellow);
  }
  .sleeve__divider {
    position: absolute; left: 0; top: 218px; width: 100%; height: 5px;
    background: var(--white);
  }
  .sleeve__band {
    position: absolute; left: 0; top: 223px; width: 100%; height: 70px;
    background: var(--black);
  }
  .pack-count {
    position: absolute; top: 9px; width: 110px; text-align: center;
    font-weight: 900; font-size: 24px; letter-spacing: 0.5px; color: var(--black);
  }
  .wordmark {
    position: absolute; top: 83px;
    white-space: nowrap;
    font-weight: 900; font-size: 52px; letter-spacing: -0.5px; color: var(--black);
    line-height: 1;
    transform: scaleX(0.75);
    transform-origin: left top;
  }
  .seal {
    position: absolute; top: 73px; width: 92px; height: 92px;
    display: flex; flex-direction: column; align-items: center; justify-content: center; gap: 6px;
  }
  .seal__dot {
    width: 44px; height: 44px; border-radius: 50%; background: var(--black);
  }
  .seal__name {
    font-weight: 900; font-size: 12px; color: var(--black); letter-spacing: 0.5px;
  }
  .certificate {
    position: absolute; left: 148px; top: 232px; width: 74px; height: 51px;
    background: var(--white);
  }
  .composition {
    position: absolute; left: 250px; top: 234px; width: 180px; text-align: right;
    color: var(--white); font-weight: 500; font-size: 7.5px; line-height: 9px;
  }
  .composition strong { font-weight: 800; }
  .care-icons {
    position: absolute; left: 292px; top: 262px; width: 138px; height: 22px;
  }
  .size-tag {
    position: absolute; top: 240px; width: 110px; text-align: center; line-height: 1;
  }
  .size-tag__label { display: block; font-weight: 900; font-size: 21px; color: var(--yellow); }
  .size-tag__size { display: block; margin-top: 4px; font-weight: 700; font-size: 15px; color: var(--white); }
  .product {
    position: absolute; left: 645px; top: 234px; line-height: 1;
  }
  .product__name { display: block; font-weight: 900; font-size: 23px; color: var(--yellow); letter-spacing: 0.3px; }
  .product__size { display: block; margin-top: 4px; font-weight: 800; font-size: 21px; color: var(--white); }
</style>
</head>
<body>
  <section class="sleeve" aria-label="Banderole Brunsdorff Arbeitssocken">
    <div class="pack-count" style="left:480px">3 PAAR</div>
    <div class="pack-count" style="left:978px">3 PAAR</div>

    <div class="wordmark" style="left:146px">BRUNSDORFF</div>
    <div class="seal" style="left:488px"><span class="seal__dot"></span><span class="seal__name">BRUNSDORFF</span></div>

    <div class="wordmark" style="left:645px">BRUNSDORFF</div>
    <div class="seal" style="left:987px"><span class="seal__dot"></span><span class="seal__name">BRUNSDORFF</span></div>

    <div class="sleeve__divider"></div>
    <div class="sleeve__band"></div>

    <div class="certificate" role="img" aria-label="Prüfsiegel Textilien"></div>

    <p class="composition">
      <strong>70%</strong> BAUMWOLLE / COTTON<br>
      COTON / KATOEN / BAVLNY<br>
      <strong>30%</strong> POLYESTER
    </p>

    <svg class="care-icons" viewBox="0 0 138 22" fill="none" stroke="#fff" stroke-width="1.3" aria-label="Pflegehinweise">
      <path d="M1 5 L4 20 H23 L26 5 M1 5 Q7 8 13 5 Q19 2 26 5"/>
      <text x="13.5" y="17" font-size="8" font-weight="700" fill="#fff" stroke="none" text-anchor="middle" font-family="Montserrat, sans-serif">60°</text>
      <path d="M32 20 L43 3 L54 20 Z M34 4 L52 20 M52 4 L34 20"/>
      <rect x="61" y="2" width="18" height="18"/><circle cx="70" cy="11" r="7"/><path d="M61 2 L79 20 M79 2 L61 20"/>
      <path d="M88 19 L92 8 H108 L112 19 Z M87 6 L113 20 M113 6 L87 20"/>
      <circle cx="127" cy="11" r="8.5"/><path d="M120 4 L134 18 M134 4 L120 18"/>
    </svg>

    <div class="size-tag" style="left:479px"><span class="size-tag__label">WORK</span><span class="size-tag__size">43-46</span></div>

    <div class="product"><span class="product__name">ARBEITS SOCKEN</span><span class="product__size">EU 43-46</span></div>

    <div class="size-tag" style="left:978px"><span class="size-tag__label">WORK</span><span class="size-tag__size">43-46</span></div>
  </section>
</body>
</html>
```